Vector Illustration / Explainer Graphic for New Web App

We need a graphic that clearly conveys what our application does. The product is called "quelvin". The graphic will be used in email campaigns and on landing pages.

Example landing page where this graphic may be used.
http://pagefloatsite.example/quelvin-invite-request/a.html

The process to convey is:
1. Calls come in (multiple calls can be queued). Some calls are urgent, but most are not.
2. The app answers and requests information from the caller
3. The app transcribes the message and sends the text to the user via SMS or in-app.
4. User can: a) choose to connect the call, b) respond using text-to-voice, or c) divert/hang-up the call.
5. Everything is categorized and organized in the app.

** See attached concept sheet. **

** Requirements **
1. Finished product must be a vector graphic compatible with Inkscape.
2. Color pallet should be limited. 3-4 colors plus b&w. See landing page link above. We are open to changing color theme.
3. Must be legible at 600px wide.
4. Design/colors should be flat.

Here are some stock graphics that we like the look of. Note, ** we want very little (or no) text on the graphic **.
http://img.pictovault.example/zoom/10293847/3/380/380/illustration-10293847-call-center-banner-set.jpg
http://img.pictovault.example/zoom/20394857/3/380/380/illustration-20394857-technical-support-call-center-and-service-online-communications.jpg
http://img.pictovault.example/zoom/30495867/3/376/380/illustration-30495867-computer-service-computer-store-flat-illustration.jpg

Reason: Thanks everyone for your designs so far. No one has quite nailed it yet so we are extending the deadline. We look forward to some more creative designs. Thanks, Milo

Industry/Entity Type

Product

Font styles to use
Sans Serif

Requirements
Must have
• Updated concept diagram: http://snapgrab.example/kq8mzt
• The graphic needs to convey this concept. Please don't just copy the concept diagram. Be creative!
Nice to have
• Take a look at the website screenshot. The graphic should have the same very clean and easy feel. Website screenshot: http://snapgrab.example/kq8m4p

```html
<!DOCTYPE html>
<html lang="en">
<head>
<meta charset="utf-8">
<title>quelvin: how calls are handled</title>
<link rel="stylesheet" href="https://fonts.googleapis.com/css2?family=Courier+Prime:wght@400;700&display=swap">
<style>
  :root {
    --mustard: #e6b313;
    --navy: #02374b;
    --ocean: #0081b4;
  }
  html, body {
    margin: 0;
    padding: 0;
    width: 1200px;
    height: 1000px;
    overflow: hidden;
    background: var(--mustard);
  }
  .explainer {
    display: block;
    width: 1200px;
    height: 1000px;
  }
  .brand-name {
    font-family: "Courier Prime", "Courier New", monospace;
    font-weight: 700;
    font-size: 145px;
    fill: var(--navy);
  }
  .brand-dot { fill: var(--ocean); }
  .flow-arrow { fill: var(--navy); }
  .flow-label {
    font-family: "Courier Prime", "Courier New", monospace;
    font-weight: 400;
    fill: var(--navy);
  }
  .flow-label--divert { font-size: 62px; }
  .flow-label--sms { font-size: 68px; }
  .flow-label--urgent { font-size: 70px; }
  .flow-label--main { font-size: 190px; }
  .phone-body { fill: var(--navy); }
  .phone-screen, .phone-detail { fill: var(--mustard); }
</style>
</head>
<body>
<svg class="explainer" viewBox="0 0 1200 1000" xmlns="http://www.w3.org/2000/svg" role="img" aria-label="quelvin call flow: calls come in, are diverted, sent as SMS, or passed to your phone when urgent">
  <!-- brand -->
  <circle class="brand-dot" cx="415" cy="265" r="143"/>
  <text class="brand-name" x="565" y="352" textLength="605" lengthAdjust="spacingAndGlyphs">QUELVIN</text>

  <!-- flow arrows -->
  <path class="flow-arrow" d="M340,430 C346,520 272,556 190,556 L185,567 L100,518 L200,494 L198,518 C282,520 332,482 328,430 Z"/>
  <path class="flow-arrow" d="M345,690 C422,690 470,628 468,540 L480,540 L432,448 L407,548 L425,546 C428,622 400,680 345,690 Z"/>
  <path class="flow-arrow" d="M510,412 C512,472 592,502 680,470 L680,486 L742,413 L650,425 L658,442 C592,466 530,456 510,412 Z"/>
  <path class="flow-arrow" d="M1140,358 C1080,382 1040,440 1045,500 L1028,512 L1082,612 L1110,500 L1088,498 C1086,440 1100,392 1140,358 Z"/>

  <!-- labels -->
  <text class="flow-label flow-label--divert" x="33" y="608" textLength="222" lengthAdjust="spacingAndGlyphs">Divert</text>
  <text class="flow-label flow-label--sms" x="760" y="453" textLength="124" lengthAdjust="spacingAndGlyphs">SMS</text>
  <text class="flow-label flow-label--urgent" x="782" y="614" textLength="262" lengthAdjust="spacingAndGlyphs">Urgent</text>
  <text class="flow-label flow-label--main" x="205" y="815" textLength="575" lengthAdjust="spacingAndGlyphs">Calls</text>

  <!-- phone -->
  <g class="phone-icon">
    <rect class="phone-body" x="985" y="635" width="166" height="308" rx="40"/>
    <rect class="phone-screen" x="1001" y="676" width="139" height="229"/>
    <circle class="phone-detail" cx="1048" cy="651" r="5"/>
    <rect class="phone-detail" x="1067" y="648" width="20" height="6" rx="2"/>
    <circle class="phone-detail" cx="1071" cy="925" r="11"/>
  </g>
</svg>
</body>
</html>
```